Massage Therapy and Personal Training Business Card (RT Restful)

I need a logo design based in Washington. The company is called RT Restful. RT are my initials. I specialize in massage therapy and personal training and general wellness of my clients. I've tried getting designs but haven't quite yet found what I'm looking for. I'm not inclined to a certain color yet but some color that resembles wellness such as light blue and white or green and white. Again, I'm not really picky about that. Thank you in advance

Industry/Entity Type

Business

Contact Information for Business Card

Have the description on one side and space for writing information on the back side such as number, appt, etc. I have an example attached. I see a lot of these card. I dont want the exact one, but something similar. Simple, professional and elegant.

Colors

Designer to choose colors to be used in the design.

Requirements
Must have
• Space on the back side to write
• A professional, elegant look
Should not have
• cartoon like style.

```html
<!DOCTYPE html>
<html lang="en">
<head>
<meta charset="utf-8">
<title>RT Restful – Business Card</title>
<link rel="stylesheet" href="https://fonts.googleapis.com/css2?family=Lora:wght@600&family=Arimo:wght@400&display=swap">
<style>
  :root {
    --backdrop: #1f1f21;
    --card: #f4f5f5;
    --card-shade: #e6e8e8;
    --teal: #5db7c6;
    --ink: #5a5a5a;
    --rule: #6a6a6a;
    --ring: #ebeded;
  }
  * { margin: 0; padding: 0; box-sizing: border-box; }
  html, body { width: 1200px; height: 900px; overflow: hidden; }
  body {
    background: var(--backdrop);
    font-family: "Arimo", Arial, sans-serif;
    display: flex;
    flex-direction: column;
    align-items: center;
    justify-content: center;
    gap: 56px;
  }
  .card {
    position: relative;
    width: 620px;
    height: 354px;
    border-radius: 26px;
    background: linear-gradient(135deg, var(--card) 0%, #ffffff 55%, var(--card-shade) 100%);
    overflow: hidden;
  }
  .card__ring {
    position: absolute;
    right: -70px;
    bottom: -40px;
  }
  .brand {
    font-family: "Lora", Georgia, serif;
    font-weight: 600;
    color: var(--teal);
    font-size: 38px;
    letter-spacing: 1px;
    line-height: 1;
  }

  /* Front */
  .front { text-align: center; padding-top: 44px; }
  .front .brand { margin-bottom: 28px; }
  .front__name {
    font-family: "Lora", Georgia, serif;
    font-weight: 600;
    font-size: 24px;
    letter-spacing: 1.5px;
    color: var(--ink);
  }
  .front__role {
    font-size: 15px;
    letter-spacing: 2px;
    color: var(--teal);
    margin-top: 6px;
    text-transform: uppercase;
  }
  .front__divider {
    width: 44px;
    height: 2px;
    background: var(--teal);
    margin: 20px auto 22px;
  }
  .front__contact { font-size: 17px; color: var(--ink); line-height: 1.55; }
  .front__address { color: var(--teal); }

  /* Back */
  .back { padding: 52px 44px 0 60px; }
  .back__top { display: flex; justify-content: space-between; }
  .back .brand { margin-top: 8px; }
  .slots { width: 300px; }
  .slot {
    display: flex;
    align-items: flex-end;
    gap: 10px;
    font-size: 17px;
    color: var(--ink);
    height: 40px;
  }
  .slot__line { flex: 1; border-bottom: 1.5px solid var(--rule); margin-bottom: 4px; }
  .services {
    position: absolute;
    left: 60px;
    right: 44px;
    bottom: 50px;
    display: flex;
    justify-content: space-between;
    list-style: none;
  }
  .services li {
    display: flex;
    align-items: center;
    gap: 10px;
    font-size: 16px;
    color: var(--ink);
  }
  .services li::before {
    content: "";
    width: 9px;
    height: 9px;
    background: var(--teal);
  }
</style>
</head>
<body>

  <section class="card front">
    <svg class="card__ring" width="260" height="260" viewBox="0 0 260 260" aria-hidden="true">
      <circle cx="130" cy="130" r="100" fill="none" stroke="var(--ring)" stroke-width="36"/>
    </svg>
    <div class="brand">RT Restful</div>
    <div class="front__name">RYAN TALBOT</div>
    <div class="front__role">Massage Theraphist</div>
    <div class="front__divider"></div>
    <div class="front__contact">
      <div>www.rtrestful.com</div>
      <div>ryan@rtrestful.com</div>
      <div class="front__address">42 Cedar Lane Road, Bellmont, WA 98001</div>
    </div>
  </section>

  <section class="card back">
    <svg class="card__ring" width="260" height="260" viewBox="0 0 260 260" aria-hidden="true">
      <circle cx="130" cy="130" r="100" fill="none" stroke="var(--ring)" stroke-width="36"/>
    </svg>
    <div class="back__top">
      <div class="brand">RT Restful</div>
      <div class="slots">
        <div class="slot"><span>No.</span><span class="slot__line"></span></div>
        <div class="slot"><span>Date:</span><span class="slot__line"></span></div>
        <div class="slot"><span>Time:</span><span class="slot__line"></span></div>
      </div>
    </div>
    <ul class="services">
      <li>Massage Theraphy</li>
      <li>Personal Training</li>
      <li>General Wellness</li>
    </ul>
  </section>

</body>
</html>
```